Whiskerwatch 4th Annual Charity Golf Tournament

We need a graphic design suitable to be displayed on a billboard to promote our golf tournament on Monday May 13th at Brenmoor Ridge Golf Course.

Target Market(s)

Golfers and potential donors for Whiskerwatch

Industry/Entity Type

Golfing

Requirements
Must have
• Date of event, sponsor logos, location of event, contact info
Nice to have
• Our tagline “the special forces of cat rescue” and photo of Brenmoor Ridge golf course if its applicable for an ad this size

```html
<!DOCTYPE html>
<html lang="en">
<head>
<meta charset="utf-8">
<title>Whiskerwatch 4th Annual Charity Golf Tournament</title>
<link rel="stylesheet" href="https://fonts.googleapis.com/css2?family=Oswald:wght@400;500;600;700&display=swap">
<style>
  :root {
    --stage: #58595b;
    --white: #ffffff;
    --green: #3fae49;
    --green-deep: #0b7a3f;
    --green-text: #1d7d3b;
    --ink: #000000;
    --charcoal: #3a3a3a;
    --silhouette: #111111;
  }
  * { box-sizing: border-box; margin: 0; padding: 0; }
  html, body { width: 1016px; height: 1200px; overflow: hidden; }
  body {
    background: var(--stage);
    font-family: "Oswald", "Arial Narrow", sans-serif;
    position: relative;
  }
  .billboard {
    position: absolute;
    left: 28px; top: 360px;
    width: 960px; height: 480px;
    background: var(--white);
    overflow: hidden;
    box-shadow: 0 24px 40px rgba(0,0,0,.45);
  }
  .band { position: absolute; left: 0; width: 100%; }
  .band--green { top: 92px; height: 170px; background: var(--green); }
  .band--deep { top: 262px; height: 51px; background: var(--green-deep); }
  .band--info { top: 313px; height: 95px; background: var(--ink); }

  .emblem {
    position: absolute; left: 47px; top: 19px;
    width: 296px; height: 296px; border-radius: 50%;
    background: var(--white);
    display: flex; align-items: center; justify-content: center;
  }
  .emblem__disc {
    width: 270px; height: 270px; border-radius: 50%;
    background: var(--charcoal);
    display: flex; align-items: center; justify-content: center;
  }
  .emblem__name {
    color: var(--white); font-weight: 700; font-size: 36px;
    letter-spacing: 1px; text-transform: uppercase;
  }

  .kicker {
    position: absolute; left: 377px; top: 44px;
    font-size: 34px; font-weight: 600; color: var(--green-text);
    letter-spacing: .5px; line-height: 1;
  }
  .title {
    position: absolute; left: 377px; top: 106px;
    font-size: 74px; font-weight: 700; color: var(--white);
    line-height: .94; letter-spacing: .5px;
    text-shadow: 3px 3px 0 var(--green-deep);
  }
  .tagline {
    position: absolute; left: 358px; top: 267px;
    font-size: 28px; font-weight: 600; color: var(--white);
    letter-spacing: .5px; line-height: 1.4;
  }
  .golfer {
    position: absolute; left: 832px; top: 14px;
    width: 100px; height: 299px;
    background: linear-gradient(180deg, #1b1b1b, var(--silhouette));
    clip-path: polygon(30% 0, 100% 0, 100% 45%, 80% 100%, 30% 100%, 20% 45%, 0 20%);
  }

  .info { position: absolute; top: 313px; height: 95px; display: flex; align-items: center; }
  .info--when { left: 40px; }
  .info--contact { left: 537px; }
  .info__icon {
    flex: none;
    width: 50px; height: 50px; border-radius: 50%;
    background: var(--green);
    display: flex; align-items: center; justify-content: center;
  }
  .info__rule { flex: none; width: 2px; height: 66px; background: var(--white); margin: 0 15px 0 15px; }
  .info__main { color: var(--white); font-size: 46px; font-weight: 600; line-height: 1; letter-spacing: .5px; }
  .info__sub { color: var(--white); font-size: 21px; font-weight: 400; line-height: 1.2; letter-spacing: 1px; margin-top: 2px; white-space: nowrap; }

  .sponsors { position: absolute; left: 0; top: 408px; width: 100%; height: 72px; }
  .sponsors__label {
    position: absolute; left: 69px; top: 23px;
    font-size: 19px; font-weight: 400; color: var(--ink); letter-spacing: .5px;
  }
  .sponsor {
    position: absolute; top: 25px; transform: translateX(-50%);
    font-size: 16px; font-weight: 600; white-space: nowrap; line-height: 1.2;
  }
  .sponsor--green { color: var(--green-text); }
  .sponsor--ink { color: var(--ink); }
</style>
</head>
<body>
  <main class="billboard">
    <div class="band band--green"></div>
    <div class="band band--deep"></div>
    <div class="band band--info"></div>

    <div class="emblem">
      <div class="emblem__disc"><span class="emblem__name">Whiskerwatch</span></div>
    </div>

    <p class="kicker">4TH ANNUAL WHISKERWATCH</p>
    <h1 class="title">CHARITY GOLF<br>TOURNAMENT</h1>
    <p class="tagline">THE SPECIAL FORCES OF CAT RESCUE</p>
    <div class="golfer" role="img" aria-label="Black silhouette of a golfer finishing a swing"></div>

    <div class="info info--when">
      <div class="info__icon">
        <svg width="26" height="30" viewBox="0 0 26 30" fill="none" stroke="#fff" stroke-width="2.6" stroke-linecap="round">
          <path d="M13 22 C8 16 5 12 5 9 A8 8 0 0 1 21 9 C21 12 18 16 13 22 Z"/>
          <circle cx="13" cy="9" r="3"/>
          <line x1="7" y1="27" x2="19" y2="27"/>
        </svg>
      </div>
      <div class="info__rule"></div>
      <div>
        <p class="info__main">MONDAY MAY 13TH</p>
        <p class="info__sub">BRENMOOR RIDGE GOLF COURSE</p>
      </div>
    </div>

    <div class="info info--contact">
      <div class="info__icon">
        <svg width="28" height="28" viewBox="0 0 28 28" fill="none" stroke="#fff" stroke-width="2.4" stroke-linecap="round" stroke-linejoin="round">
          <path d="M7 4 L11 9 L9 12 C10 15 13 18 16 19 L19 17 L24 21 L21 25 C13 24 4 15 3 7 Z"/>
          <path d="M16 8 A5 5 0 0 1 20 12"/>
          <path d="M16 3 A10 10 0 0 1 25 12"/>
        </svg>
      </div>
      <div class="info__rule"></div>
      <div>
        <p class="info__main">800 555.0142</p>
        <p class="info__sub">WWW.WHISKERWATCHGOLF.COM</p>
      </div>
    </div>

    <section class="sponsors">
      <p class="sponsors__label">SPONSORED BY</p>
      <span class="sponsor sponsor--ink" style="left:314px">WHISKERWATCH</span>
      <span class="sponsor sponsor--ink" style="left:477px">FAIRWAY OUTFITTERS</span>
      <span class="sponsor sponsor--green" style="left:634px">HARROW ISLES</span>
      <span class="sponsor sponsor--ink" style="left:752px">ASHBY LAW</span>
      <span class="sponsor sponsor--ink" style="left:878px">COASTLINE DECKS</span>
    </section>
  </main>
</body>
</html>
```